1) This is a self-help business book for women executives and entrepreneurs that will assist women in getting to the next level of success. The reader should feel confident that this book will solve their problem in elevating their current position.
2) The primary message I want to convey on the cover is that they are in the right hands to solve their issue of promoting themselves, without losing themselves or the ones they love. Women can have it all!
3) Can be a realistic sketch of: I envision a woman sitting on a Queen Anne white chair (victorian style tufted in diamonds) with dark brown / reddish highlights in hair. She has almond/light brown skin.
She is dressed professionally - see attached pic in red dress - change to navy blue dress w/ solid nude pumps. Her hand is out holding a diamond paperweight. The light beam hits the bottom of the paperweight and fractures out to gold and silver sparkles (like 3D sparkles). The 4 corners of the book cover to include gold and silver matte damask.
Like purple title in a font with curves. Preferred book colors: white, gold, silver, purple
4) The setting of the book in a modern and current day for executive women.
5) Book Title -- The Lantern Ledger
Subtitle -- Climb the Ladder and Still Keep Every Evening for Family
6) Author -- Dr. Marla Quentin
7) ebook size - 4 1/2 x 7 1/2, cover 7.3, not more than 50Mb, 2560x 1600 jpg
8) See attached example of Queen Anne white Chair tufted w/ diamonds and flap copy book description
9) see attached example of diamond refracting light (not rainbow - gold / silver )
Idea 2 -----
Woman hand holding diamond paperweight; can see glimmer of facets within diamond;singular white light towards one side of diamond and the other side refracts with gold / silver glistens (see pic - not rainbow as an pic)

```html
<!DOCTYPE html>
<html lang="en">
<head>
<meta charset="utf-8">
<title>The Lantern Ledger — Cover Spread</title>
<link rel="stylesheet" href="https://fonts.googleapis.com/css2?family=Michroma&family=Arimo:wght@400;700&display=swap">
<style>
  :root {
    --stage-light: #f4f4f4;
    --stage-dark: #c9c9c9;
    --cover-white: #ffffff;
    --back-black: #1c1c1c;
    --back-black-edge: #2a2a2a;
    --back-text: #f2f2f2;
    --back-muted: #8a8a8a;
    --ink: #111111;
    --title-warm-1: #3a2b2e;
    --title-warm-2: #9a7f86;
    --title-warm-3: #caa595;
    --title-warm-4: #5b4650;
    --portrait-1: #2a1c20;
    --portrait-2: #7a5a52;
    --portrait-3: #b48c78;
    --portrait-4: #2d4f9a;
  }
  * { margin: 0; padding: 0; box-sizing: border-box; }
  html, body {
    width: 1200px;
    height: 800px;
    overflow: hidden;
  }
  body {
    background: radial-gradient(ellipse at 50% 45%, var(--stage-light) 0%, #e6e6e6 55%, var(--stage-dark) 100%);
    position: relative;
  }

  /* Back cover */
  .back-cover {
    position: absolute;
    left: 205px;
    top: 122px;
    width: 370px;
    height: 555px;
    background: linear-gradient(90deg, var(--back-black-edge) 0%, var(--back-black) 40%, var(--back-black) 100%);
    box-shadow: 0 6px 24px rgba(0,0,0,0.22);
    padding: 120px 44px 0 44px;
    font-family: "Arimo", sans-serif;
    color: var(--back-text);
  }
  .back-copy {
    font-size: 9.5px;
    line-height: 1.55;
    margin-bottom: 14px;
  }
  .back-callout {
    font-weight: 700;
    font-size: 11px;
    letter-spacing: 0.6px;
    text-align: center;
    margin: 20px 0 18px;
  }
  .back-visit {
    font-weight: 700;
    font-size: 9.5px;
    line-height: 1.3;
    text-align: center;
    text-transform: uppercase;
    margin-top: 22px;
  }
  .back-web {
    font-size: 9.5px;
    letter-spacing: 0.8px;
    text-align: center;
    text-transform: uppercase;
    color: var(--back-muted);
    margin-top: 14px;
  }

  /* Front cover */
  .book-cover {
    position: absolute;
    left: 625px;
    top: 122px;
    width: 370px;
    height: 555px;
    background: var(--cover-white);
    box-shadow: 0 6px 24px rgba(0,0,0,0.18);
  }
  .cover-title {
    position: absolute;
    top: 74px;
    left: 0;
    width: 100%;
    text-align: center;
    font-family: "Michroma", sans-serif;
    font-weight: 400;
    font-size: 30px;
    line-height: 1.08;
    letter-spacing: 0.3px;
    -webkit-text-stroke: 0.6px var(--title-warm-1);
    background: linear-gradient(100deg, var(--title-warm-1) 0%, var(--title-warm-2) 25%, var(--title-warm-4) 45%, var(--title-warm-3) 65%, var(--title-warm-1) 85%, var(--title-warm-2) 100%);
    -webkit-background-clip: text;
    background-clip: text;
    color: transparent;
  }
  .cover-subtitle {
    position: absolute;
    top: 160px;
    left: 45px;
    width: 280px;
    text-align: center;
    font-family: "Arimo", sans-serif;
    font-weight: 700;
    font-size: 8.5px;
    line-height: 1.15;
    text-transform: uppercase;
    color: var(--ink);
  }
  .cover-portrait {
    position: absolute;
    left: 0;
    top: 0;
    width: 370px;
    height: 555px;
  }
  .cover-author {
    position: absolute;
    top: 490px;
    left: 0;
    width: 100%;
    text-align: center;
    font-family: "Michroma", sans-serif;
    font-size: 20px;
    -webkit-text-stroke: 0.5px var(--ink);
    color: var(--ink);
    letter-spacing: 0.3px;
  }
</style>
</head>
<body>
  <section class="back-cover">
    <p class="back-copy">Every leader reaches a point where the next step feels like a trade between ambition and home. This book shows a calmer route upward, with clear habits that build influence while protecting the people and hours that matter most.</p>
    <p class="back-copy">Inside you will find plain tools for asking, pitching and leading, drawn from years of coaching women who run teams, firms and families at once.</p>
    <p class="back-copy">Read it in one weekend, then keep it close. Each chapter ends with a short plan you can start on Monday morning.</p>
    <p class="back-callout">PLACE YOUR 6 X 9 BLURB HERE</p>
    <p class="back-copy">Dr. Quentin speaks, writes and coaches from her home office, where dinner still starts at six.</p>
    <p class="back-visit">Visit the authors<br>website at:</p>
    <p class="back-web">www.marlaquentin.com</p>
  </section>

  <main class="book-cover">
    <h1 class="cover-title">THE LANTERN<br>LEDGER</h1>
    <p class="cover-subtitle">Climb the ladder and still keep<br>every evening for family</p>
    <svg class="cover-portrait" viewBox="0 0 480 720" role="img" aria-label="Portrait of the author smiling, holding a faceted crystal paperweight that catches a beam of light, against a sparkling sequined backdrop">
      <defs>
        <linearGradient id="portrait-tone" x1="0" y1="0" x2="1" y2="1">
          <stop offset="0" stop-color="var(--portrait-2)"/>
          <stop offset="0.35" stop-color="var(--portrait-1)"/>
          <stop offset="0.6" stop-color="var(--portrait-3)"/>
          <stop offset="0.85" stop-color="var(--portrait-1)"/>
          <stop offset="1" stop-color="var(--portrait-4)"/>
        </linearGradient>
      </defs>
      <polygon points="205,290 420,400 365,590 210,590 70,440" fill="url(#portrait-tone)"/>
    </svg>
    <p class="cover-author">DR. MARLA QUENTIN</p>
  </main>
</body>
</html>
```